Tarrant keystone graphic

We need a graphic for an offer in our dental office for Tarrant keystone treatment. Once enrolled the patient will be given a whitening treatment once a year for as long as they are a patient with our office. This means that they must come in for their routine cleanings. Fine print: There is an enrollment fee of 99 dollars and contact us for additional rules and conditions. We need a logo or picture that we can use on our home page slide show that is clean and makes you think of healthy white teeth. Our logo to our practice has been enclosed as well to give you style direction. We don't want this logo to have a ton of wording on it, it needs to be clean and modern looking. The name of the program is call Tarrant Keystone and we need to have the fine print on the ad as well, but we will be looking for entries that incorporate our logo that is submitted and can make this offer really stand out.

Industry/Entity Type

Dental

```html
<!DOCTYPE html>
<html lang="en">
<head>
<meta charset="utf-8">
<title>Tarrant Keystone – harbor point dental studio</title>
<link rel="stylesheet" href="https://fonts.googleapis.com/css2?family=Mulish:wght@300;400;500&family=Parisienne&display=swap">
<style>
  :root {
    --bg-centre: #ffffff;
    --bg-mid: #e4f2f5;
    --bg-edge: #9fcfd9;
    --ink-dark: #1d3c44;
    --ink-title: #3e6a6d;
    --ink-fine: #4e6d72;
    --tooth-light: #ffffff;
    --tooth-shade: #d7dcdf;
  }
  html, body {
    margin: 0;
    padding: 0;
    overflow: hidden;
    background: var(--bg-edge);
  }
  .slide {
    position: relative;
    width: 1200px;
    height: 654px;
    overflow: hidden;
    background: radial-gradient(ellipse 75% 80% at 42% 42%, var(--bg-centre) 0%, var(--bg-mid) 55%, var(--bg-edge) 100%);
    font-family: "Mulish", sans-serif;
  }
  .tooth-visual {
    position: absolute;
    left: 90px;
    top: 198px;
    width: 198px;
    height: 264px;
    border-radius: 46% 46% 30% 30%;
    background: radial-gradient(circle at 38% 30%, var(--tooth-light) 0%, #f2f4f5 45%, var(--tooth-shade) 100%);
  }
  .practice {
    position: absolute;
    left: 360px;
    width: 750px;
    text-align: center;
    color: var(--ink-dark);
  }
  .practice-name {
    top: 240px;
    margin: 0;
    font-size: 53px;
    font-weight: 500;
    letter-spacing: 0.5px;
    line-height: 1;
  }
  .practice-doctors {
    top: 310px;
    margin: 0;
    font-size: 26px;
    font-weight: 500;
    line-height: 1;
  }
  .practice-doctors .divider {
    display: inline-block;
    width: 2px;
    height: 28px;
    margin: 0 4px;
    background: var(--ink-dark);
    vertical-align: -5px;
  }
  .program-title {
    position: absolute;
    left: 300px;
    top: 408px;
    width: 860px;
    margin: 0;
    text-align: center;
    font-family: "Parisienne", cursive;
    font-weight: 400;
    font-size: 76px;
    letter-spacing: 14px;
    line-height: 1;
    color: var(--ink-title);
    text-shadow: 4px 6px 6px rgba(40, 70, 75, 0.35);
  }
  .fine-print {
    position: absolute;
    left: 0;
    bottom: 10px;
    width: 1200px;
    margin: 0;
    text-align: center;
    font-size: 20px;
    font-weight: 300;
    letter-spacing: 2px;
    color: var(--ink-fine);
  }
</style>
</head>
<body>
  <main class="slide">
    <div class="tooth-visual" role="img" aria-label="Glossy white molar tooth illustration"></div>
    <h2 class="practice practice-name">harbor point dental studio</h2>
    <p class="practice practice-doctors">Dr Ellis Warren<span class="divider"></span>Dr Mina Cho</p>
    <h1 class="program-title">Tarrant Keystone</h1>
    <p class="fine-print">There is an enrollment fee of 99 dollars and contact us for additional rules and conditions.</p>
  </main>
</body>
</html>
```